BLORK Business Card

Quellmont Dwelling Additions and Refits. I need a business card designed for this new high end renovation business. I would like the logo centered on the back side with the ABN (71 903 226 417) on the bottom right hand corner.

I would like the following information placed on the other side along with some customized pattern or design.

Percival Oakden
Director
Phone: 1300 418 957
Fax: (02) 9316 4471
Website: www.blorkbuilding.com.au
Email: p.oakden@blorkbuilding.com.au
PO Box 87,
Wendlecove NSW 2094

(FB Logo) BLORK - Quellmont Dwelling Additions and Refits

The final design should communicate professionalism and trust.

Back side background colour: white
Front side: Undecided

```html
<!DOCTYPE html>
<html lang="en">
<head>
<meta charset="utf-8">
<title>BLORK Business Card</title>
<link rel="stylesheet" href="https://fonts.googleapis.com/css2?family=Cinzel:wght@400;600&family=EB+Garamond:wght@400;500&display=swap">
<style>
  :root {
    --backdrop: #2b2b2b;
    --card: #ffffff;
    --brand-blue: #1d4f91;
    --band-blue: #0e4a8a;
    --band-blue-light: #1a5ea6;
    --band-edge: #c9ced6;
    --logo-grey: #333537;
    --ink: #222222;
    --tile-grey: #dcdada;
    --badge-blue: #3f8fd6;
    --badge-blue-light: #a9d0f2;
  }
  html, body {
    margin: 0;
    padding: 0;
    width: 1000px;
    height: 1200px;
    overflow: hidden;
    background: var(--backdrop);
  }
  .canvas {
    position: relative;
    width: 1000px;
    height: 1200px;
  }
  .card {
    position: absolute;
    width: 723px;
    height: 422px;
    background: var(--card);
    box-shadow: 0 4px 14px rgba(0,0,0,0.45);
    overflow: hidden;
  }
  .card--front { left: 145px; top: 72px; }
  .card--back  { left: 139px; top: 637px; }

  /* Front side */
  .person {
    position: absolute;
    right: 34px;
    top: 52px;
    text-align: right;
  }
  .person__name {
    font-family: "Cinzel", serif;
    font-size: 20px;
    color: var(--brand-blue);
    letter-spacing: 0.5px;
    line-height: 26px;
  }
  .person__role {
    font-family: "EB Garamond", serif;
    font-size: 18px;
    color: var(--ink);
    line-height: 20px;
  }
  .wordmark {
    position: absolute;
    left: 0;
    right: 0;
    text-align: center;
    font-family: "Cinzel", serif;
    font-weight: 600;
    color: var(--logo-grey);
    line-height: 1;
  }
  .card--front .wordmark { top: 106px; font-size: 70px; letter-spacing: 2px; }
  .card--back .wordmark  { top: 132px; font-size: 96px; letter-spacing: 3px; }

  .tagline {
    position: absolute;
    left: 0;
    right: 0;
    text-align: center;
    font-family: "Cinzel", serif;
    color: var(--brand-blue);
    white-space: nowrap;
  }
  .card--front .tagline { top: 176px; font-size: 15px; }
  .card--back .tagline  { top: 230px; font-size: 20px; }

  .contact-band {
    position: absolute;
    left: 0;
    right: 0;
    top: 213px;
    height: 105px;
    background: linear-gradient(180deg, var(--band-blue-light), var(--band-blue));
    border-top: 3px solid var(--band-edge);
    border-bottom: 3px solid var(--band-edge);
    box-sizing: border-box;
  }
  .contact {
    position: absolute;
    font-family: "EB Garamond", serif;
    font-size: 18px;
    color: #ffffff;
    white-space: nowrap;
    display: flex;
    align-items: center;
    gap: 6px;
    line-height: 20px;
  }
  .contact svg { width: 16px; height: 16px; flex: none; }
  .contact--left  { right: 392px; }
  .contact--right { left: 392px; }
  .contact--row1 { top: 24px; }
  .contact--row2 { top: 53px; }
  .window-mark {
    position: absolute;
    left: 347px;
    top: 29px;
    width: 30px;
    height: 30px;
  }
  .social-badge {
    position: absolute;
    left: 325px;
    top: 292px;
    width: 64px;
    height: 64px;
    background: linear-gradient(135deg, var(--badge-blue-light), var(--badge-blue));
    border: 2px solid #ffffff;
    box-shadow: 0 2px 5px rgba(0,0,0,0.3);
  }
  .footer-line {
    position: absolute;
    left: 0;
    right: 0;
    top: 362px;
    text-align: center;
    font-family: "EB Garamond", serif;
    font-size: 17px;
    color: var(--ink);
  }

  /* Back side */
  .abn {
    position: absolute;
    left: 0;
    right: 0;
    top: 266px;
    text-align: center;
    font-family: "EB Garamond", serif;
    font-size: 20px;
    color: var(--ink);
  }
  .address-bar {
    position: absolute;
    left: 35px;
    top: 301px;
    width: 551px;
    height: 40px;
    background: var(--band-blue);
    color: #ffffff;
    font-family: "EB Garamond", serif;
    font-size: 17px;
    line-height: 40px;
    text-align: center;
  }
  .window-tiles {
    position: absolute;
    left: 587px;
    top: 271px;
    width: 102px;
    height: 98px;
  }
</style>
</head>
<body>
<main class="canvas">

  <section class="card card--front" aria-label="Card front">
    <div class="person">
      <div class="person__name">PERCIVAL OAKDEN</div>
      <div class="person__role">Director</div>
    </div>

    <div class="wordmark">BLORK</div>
    <div class="tagline">— QUELLMONT DWELLING ADDITIONS &amp; REFITS —</div>

    <div class="contact-band">
      <div class="contact contact--left contact--row1">
        1300 418 957
        <svg viewBox="0 0 16 16" aria-hidden="true"><path fill="#fff" d="M3.5 1.5l2.3 0 1 3.2-1.5 1.2c.8 1.8 2.1 3.1 3.9 3.9l1.2-1.5 3.2 1v2.3c0 .8-.7 1.4-1.5 1.4C6.7 13 3 9.3 2.1 3c0-.8.6-1.5 1.4-1.5z"/></svg>
      </div>
      <div class="contact contact--left contact--row2">
        www.blorkbuilding.com.au
        <svg viewBox="0 0 16 16" aria-hidden="true"><g fill="none" stroke="#fff" stroke-width="1.4"><circle cx="8" cy="8" r="6.3"/><path d="M2 8h12M8 1.7c-2.5 3-2.5 9.6 0 12.6M8 1.7c2.5 3 2.5 9.6 0 12.6"/></g></svg>
      </div>

      <svg class="window-mark" viewBox="0 0 30 30" aria-hidden="true">
        <rect x="0" y="0" width="13" height="13" fill="#fff"/>
        <rect x="17" y="0" width="13" height="13" fill="#fff"/>
        <rect x="0" y="17" width="13" height="13" fill="#fff"/>
        <rect x="17" y="17" width="13" height="13" fill="#fff"/>
      </svg>

      <div class="contact contact--right contact--row1">
        <svg viewBox="0 0 16 16" aria-hidden="true"><path fill="#fff" d="M4 1h6l2 2v3H4zM2 7h12v6H2zM5 9h6v1H5z"/></svg>
        (02) 9316 4471
      </div>
      <div class="contact contact--right contact--row2">
        <svg viewBox="0 0 16 16" aria-hidden="true"><rect x="1.5" y="3.5" width="13" height="9" fill="none" stroke="#fff" stroke-width="1.4"/><path d="M1.5 3.5l6.5 5 6.5-5" fill="none" stroke="#fff" stroke-width="1.4"/></svg>
        p.oakden@blorkbuilding.com.au
      </div>
    </div>

    <div class="social-badge" role="img" aria-label="Social page badge"></div>

    <div class="footer-line">BLORK - Quellmont Dwelling Additions and Refits</div>
  </section>

  <section class="card card--back" aria-label="Card back">
    <div class="wordmark">BLORK</div>
    <div class="tagline">— QUELLMONT DWELLING ADDITIONS &amp; REFITS —</div>
    <div class="abn">ABN (71 903 226 417)</div>
    <div class="address-bar">PO Box 87, Wendlecove NSW 2094</div>
    <svg class="window-tiles" viewBox="0 0 102 98" aria-hidden="true">
      <rect x="0" y="0" width="41" height="41" fill="var(--tile-grey)"/>
      <rect x="60" y="0" width="42" height="41" fill="var(--tile-grey)"/>
      <rect x="0" y="57" width="41" height="41" fill="var(--tile-grey)"/>
      <rect x="60" y="57" width="42" height="41" fill="var(--tile-grey)"/>
    </svg>
  </section>

</main>
</body>
</html>
```